Creating a Label for a new CBD Vape Line call "Brizel".

This will be a project that will create the first label design on a BRIZEL Vape product that is being rolled out in Colorado. The vape line will cater to high concentration CBD Vape sold in disposable vape pens and replacement cartridge's. In the sea of vape pens we want our packaging to stand out with a bold, bright, clean, abstract design that will highlight the brand "BRIZEL" in a font that stands out and is quickly recognized. The target demographic for this line is 18-29 years of age. The mock up of the brizel vape picture does not meet our marketing desire, I just wanted to show you the approximate shape and size of the label and that the font used for the label will be added to the actual pen. This pen will have 100% CBD, cut with all natural terpenes with no need for chemicals like PG or VG, not many on the market like that. I included several marketing logos that caught our eye with other type product, please look at those as examples but we are open to creativity.

Target Market(s)

18-29 year old

Industry/Entity Type

CBD and Vape

Font styles to use
Serif
Sans Serif

Requirements
Must have
• bold, colorful, fun, eye catching
Nice to have
• Several brand ideas presented to give the flavor of the marketing. The example font on the prototype is not 'cool enough' to use, we'd like that name BRIZEL to look and feel brizzzel. :-)
Should not have
• old school, boring, dull colors, small font

```html
<!DOCTYPE html>
<html lang="en">
<head>
<meta charset="utf-8">
<title>Brizel Vape – Label Concepts</title>
<link rel="stylesheet" href="https://fonts.googleapis.com/css2?family=Arimo:ital,wght@0,700;1,700&family=Oswald:wght@600&display=swap">
<style>
  :root{
    --page:#ffffff;
    --frame:#3a3a3a;
    --ink:#231f20;
    --white:#ffffff;
    --sky-top:#2fb7ee;
    --sky-bottom:#38d6ea;
    --night:#231f20;
    --logo-blue:#1a8fd0;
    --mist:#cfcfcf;
    --ruby:#e21f26;
    --pen:#2a2a2c;
    --pen-edge:#46474b;
  }
  *{box-sizing:border-box;margin:0;padding:0}
  html,body{width:1200px;height:761px;overflow:hidden;background:var(--page)}
  .canvas{position:relative;width:1200px;height:761px;border:1px solid var(--frame);background:var(--page)}
  .label{position:absolute;top:54px;width:330px;height:662px;overflow:hidden;border:1px solid var(--frame)}
  .label--rainbow{left:40px;background:var(--white)}
  .label--sky{left:427px;background:var(--night)}
  .label--mist{left:812px;background:var(--mist)}

  .art{position:absolute;left:0;top:0;width:100%}
  .art--rainbow{height:504px;background:
      linear-gradient(120deg,#e84a6b 0%,#f08a3c 18%,#f6d23a 32%,#5cbf4a 46%,#2aa7c9 60%,#3a57b8 74%,#7b3fa0 86%,#c63a4d 100%)}
  .art--sky{height:448px;background:linear-gradient(180deg,var(--sky-top),var(--sky-bottom))}
  .swirl{position:absolute;border-radius:50%;filter:blur(6px)}
  .swirl--warm{left:60px;top:-20px;width:160px;height:330px;
      background:linear-gradient(160deg,#e0306e,#f38a3a 55%,#f6c54a);transform:rotate(-12deg)}
  .swirl--cool{left:120px;top:280px;width:70px;height:180px;
      background:linear-gradient(180deg,#b9a7d6,#5a8fd8);transform:rotate(8deg)}
  .swirl--red{left:40px;top:-30px;width:190px;height:720px;
      background:linear-gradient(175deg,#b01020,var(--ruby) 40%,#f0452e 70%,#b01020);transform:rotate(6deg);filter:blur(4px)}

  .pen{position:absolute;width:40px;height:320px;border-radius:4px;
      background:linear-gradient(90deg,var(--pen) 0%,var(--pen-edge) 50%,var(--pen) 100%)}
  .pen--a{left:60px;top:200px;transform:rotate(-24deg)}
  .pen--b{left:150px;top:230px;transform:rotate(-24deg)}
  .pen--c{left:204px;top:200px;width:42px;height:370px;transform:rotate(22deg)}
  .pen--d{left:236px;top:290px;width:42px;height:360px;transform:rotate(15deg)}

  .badge{position:absolute;left:140px;top:28px;width:188px;height:188px;border-radius:50%;background:var(--ink)}
  .specs{position:absolute;font-family:"Arimo",Arial,sans-serif;font-style:italic;font-weight:700;
      font-size:16px;line-height:20px;color:var(--white);z-index:2}
  .specs--badge{left:162px;top:100px}
  .specs--sky{left:32px;top:568px}
  .specs--mist{left:32px;top:568px}

  .wordmark{position:absolute;font-family:"Arimo",Arial,sans-serif;font-weight:700;white-space:nowrap}
  .wordmark--rainbow{left:40px;top:556px;font-size:48px;color:var(--ink)}
  .logo-box{position:absolute;display:flex;align-items:center;justify-content:center;z-index:1}
  .logo-box--sky{left:23px;top:228px;width:184px;height:56px;background:var(--white)}
  .logo-box--sky .wordmark{position:static;font-family:"Oswald",sans-serif;font-weight:600;font-size:40px;line-height:1;color:var(--logo-blue);letter-spacing:1px}
  .logo-box--mist{left:100px;top:60px;width:108px;height:216px;background:var(--ruby);border:3px solid var(--white)}
  .logo-box--mist .wordmark{position:static;font-family:"Oswald",sans-serif;font-weight:600;font-size:44px;color:var(--white);transform:rotate(-90deg);letter-spacing:1px}

  .tagline{position:absolute;font-family:"Arimo",Arial,sans-serif;font-weight:700;font-size:7px;letter-spacing:2px;
      white-space:nowrap;transform-origin:left top;transform:rotate(-90deg);z-index:2}
  .tagline--sky{left:221px;top:300px;color:var(--white)}
  .tagline--mist{left:214px;top:300px;color:var(--frame);font-size:8px;letter-spacing:3px}
</style>
</head>
<body>
<main class="canvas">

  <section class="label label--rainbow">
    <div class="art art--rainbow" role="img" aria-label="Photo of fanned rainbow-coloured paper strips"></div>
    <div class="pen pen--a" role="img" aria-label="Disposable vape pen product photo"></div>
    <div class="pen pen--b" role="img" aria-label="Disposable vape pen product photo"></div>
    <div class="badge"></div>
    <p class="specs specs--badge">450mg CBD<br>LumaVAPE<br>brizelCBD.com</p>
    <p class="wordmark wordmark--rainbow">Brizel Vape</p>
  </section>

  <section class="label label--sky">
    <div class="art art--sky">
      <div class="swirl swirl--warm" role="img" aria-label="Abstract flowing colour ribbon illustration"></div>
      <div class="swirl swirl--cool"></div>
    </div>
    <div class="logo-box logo-box--sky"><span class="wordmark">BRIZEL</span></div>
    <p class="tagline tagline--sky">CREATIVE COLOR FLOW</p>
    <div class="pen pen--c" role="img" aria-label="Disposable vape pen product photo"></div>
    <p class="specs specs--sky">450mg CBD<br>LumaVAPE<br>brizelCBD.com</p>
  </section>

  <section class="label label--mist">
    <div class="swirl swirl--red" role="img" aria-label="Abstract flowing red ribbon illustration"></div>
    <div class="logo-box logo-box--mist"><span class="wordmark">BRIZEL</span></div>
    <p class="tagline tagline--mist">TRENDY VECTOR DESIGN</p>
    <div class="pen pen--d" role="img" aria-label="Disposable vape pen product photo"></div>
    <p class="specs specs--mist">450mg CBD<br>LumaVAPE<br>brizelCBD.com</p>
  </section>

</main>
</body>
</html>
```